Medical Eye Care Practice needs a unique business card design.

I need a business card for my medical, eye care practice. I am seeking a unique design, possibly with a vertical or atypical shape layout -- something to make the card stand out. I would like the final design to communicate health and wellness with a contemporary feel. Please incorporate my logo and slogan with a color scheme based off of my logo. It should also identify all of the information that is listed on my sample business card. The back side should be utilized for appointment reminder with date, time, and room for notes. I would also like some incorporation of facebook, twitter, and google plus links.

```html
<!DOCTYPE html>
<html lang="en">
<head>
<meta charset="utf-8">
<title>Lakeview Vision Care &amp; Wellbeing – Business Card</title>
<link rel="stylesheet" href="https://fonts.googleapis.com/css2?family=Lato:wght@400;700&display=swap">
<style>
  :root {
    --backdrop: #c9cacc;
    --leaf: #a6b85d;
    --leaf-text: #97b04a;
    --bark: #86705a;
    --sky: #a9cfe6;
    --paper: #ffffff;
  }
  * { margin: 0; padding: 0; box-sizing: border-box; }
  html, body { width: 1200px; height: 800px; overflow: hidden; }
  body {
    background: var(--backdrop);
    font-family: "Lato", Arial, sans-serif;
    position: relative;
  }
  .card {
    position: absolute;
    top: 120px;
    width: 340px;
    height: 560px;
    border-radius: 14px;
    text-align: center;
  }
  .card-front { left: 220px; background: var(--leaf); color: var(--paper); }
  .card-back  { left: 640px; background: var(--paper); }

  .brand { padding-top: 40px; }
  .brand-mark { display: block; margin: 0 auto 10px; }
  .brand-name {
    color: var(--bark);
    font-weight: 400;
    letter-spacing: 1px;
    line-height: 1.15;
  }
  .brand-name .primary { display: block; font-size: 33px; }
  .brand-name .secondary { display: block; font-size: 14px; letter-spacing: 1.2px; }
  .brand-rule { width: 270px; height: 1px; background: var(--bark); margin: 7px auto 6px; opacity: .8; }
  .slogan { color: var(--sky); font-size: 10.5px; letter-spacing: 1px; }
  .web { color: var(--sky); font-size: 11px; }

  .person { margin-top: 30px; }
  .person-name { color: var(--bark); font-size: 25px; font-weight: 400; letter-spacing: 1px; }
  .person-title { color: var(--sky); font-size: 15px; letter-spacing: 1px; }

  .contact { list-style: none; margin: 14px 0 0 92px; text-align: left; font-size: 16px; letter-spacing: .5px; }
  .contact li { display: flex; align-items: center; gap: 12px; margin-bottom: 8px; }
  .address { margin-top: 14px; font-size: 16px; line-height: 1.5; }

  .social { display: flex; justify-content: center; gap: 12px; margin-top: 16px; }
  .social span { width: 26px; height: 26px; border-radius: 50%; background: var(--sky); }

  .services { margin-top: 16px; font-size: 13.5px; font-weight: 700; line-height: 1.4; white-space: nowrap; }

  .card-back .brand { padding-top: 60px; }
  .appointment-title { color: var(--bark); font-size: 24px; letter-spacing: 1px; margin-top: 40px; font-weight: 400; }
  .appointment-fields { list-style: none; text-align: left; margin: 50px 0 0 40px; color: var(--leaf-text); font-size: 18px; }
  .appointment-fields li { margin-bottom: 24px; }
  .back-contact { position: absolute; right: 30px; bottom: 34px; text-align: right; color: var(--bark); font-size: 17px; line-height: 1.5; }
</style>
</head>
<body>
  <section class="card card-front">
    <header class="brand">
      <svg class="brand-mark" width="44" height="44" viewBox="0 0 44 44" aria-hidden="true">
        <circle cx="22" cy="22" r="20" fill="var(--paper)"/>
      </svg>
      <h1 class="brand-name"><span class="primary">LAKEVIEW</span><span class="secondary">VISION CARE &amp; WELLBEING</span></h1>
      <div class="brand-rule"></div>
      <p class="slogan">SEE CLEARLY • LIVE WELL • EVERY DAY</p>
      <p class="web">www.lakeview-eyecare.com</p>
    </header>

    <div class="person">
      <h2 class="person-name">EVAN HALE</h2>
      <p class="person-title">OD, FAAO</p>
    </div>

    <ul class="contact">
      <li>
        <svg width="16" height="16" viewBox="0 0 24 24" aria-label="Phone"><path fill="var(--bark)" d="M6.6 10.8a15 15 0 0 0 6.6 6.6l2.2-2.2a1 1 0 0 1 1-.25 11.4 11.4 0 0 0 3.6.6 1 1 0 0 1 1 1V20a1 1 0 0 1-1 1A17 17 0 0 1 3 4a1 1 0 0 1 1-1h3.5a1 1 0 0 1 1 1c0 1.25.2 2.45.6 3.6a1 1 0 0 1-.25 1z"/></svg>
        (414) 555- 0182
      </li>
      <li>
        <svg width="16" height="16" viewBox="0 0 24 24" aria-label="Fax"><path fill="var(--bark)" d="M6 2h12v5H6zM3 8h18a1 1 0 0 1 1 1v8h-4v5H6v-5H2V9a1 1 0 0 1 1-1zm5 8v4h8v-4z"/></svg>
        (414) 555- 0183
      </li>
    </ul>

    <p class="address">2710 Birch Ave, Suite 310,<br>Alder Falls, WI 53999</p>

    <div class="social" aria-label="Social media links">
      <span></span><span></span><span></span>
    </div>

    <p class="services">Family Eye Care, Low Vision Rehabilitation,<br>Urgent Care, Ocular Disease, Dry Eye,<br>Retinal Wellness, Ocular Nutrition</p>
  </section>

  <section class="card card-back">
    <header class="brand">
      <svg class="brand-mark" width="44" height="44" viewBox="0 0 44 44" aria-hidden="true">
        <circle cx="22" cy="22" r="20" fill="var(--sky)"/>
      </svg>
      <h1 class="brand-name"><span class="primary">LAKEVIEW</span><span class="secondary">VISION CARE &amp; WELLBEING</span></h1>
      <div class="brand-rule"></div>
      <p class="slogan">SEE CLEARLY • LIVE WELL • EVERY DAY</p>
      <p class="web">www.lakeview-eyecare.com</p>
    </header>

    <h2 class="appointment-title">APPOINTMENT</h2>
    <ul class="appointment-fields">
      <li>Date:</li>
      <li>Time:</li>
      <li>Reason for Visit:</li>
    </ul>

    <p class="back-contact">www.lakeview-eyecare.com<br>(414) 555- 0182</p>
  </section>
</body>
</html>
```